Creation of Brelto Promo remarketing banners / Creation of Brelto Promo remarketing banners

Hello!
Name: Korvi Media
Website: https://korvimedia.ca/
Activity sector: Website creation
Project: Creation of web banners
Description:
We are a web marketing agency specializing in website design. For a Brelto Promo remarketing campaign, we need:
- 6 banners each with a different background and different text in 300 x 250 px format (300 wide and 250 high).
On the design side, we want the banner to be:
- Simple and refined
- In the colors of our company: green, blue and gray (see our website)
- With a background image that represents the website design (a computer, a tablet, a cell phone, etc.)
For the design, we must take the example of the PageLoom model (attached file).
On the writing side, each banner must have a sentence and a call to action (different clickable button).
Example: In the Tundrel model, first image at the top left), there is the phrase “Be fast, flexible, secure. "And the call to action" Upgrade your Tundrel ".
Here are the 6 different texts to put on the banners (sentence + call to action):
1) Phrase: "Your phone should ring now"
Call to action: "Get a website"
2) Phrase: "One click away from success"
3) Phrase: "Boost your income online"
4) Phrase: "Win new customers"
5) Phrase: "Be where your customers are looking for you"
6) Phrase: "Increase your turnover"
On the font side, it would be good to take the example of the Tundrel banners (attached file) by putting words in front with a larger font (vary the sizes of the words of the same sentence to put the emphasis).
Thank you!
VERSION FRANCAISE
Hello!
Company name: Korvi Media
Sector of activity: Website creation
Description:
We are a web marketing agency specialized in website creation. For a Brelto Promo remarketing campaign, we need:
- 6 banners each with a different background and a different text in 300 x 250 px format (300 width and 250 height).
- Simple and uncluttered
- With a background image that represents the design of a website (a computer, tablet, mobile, etc.).
For the design, we must take the PageLoom template (in attachment) as an example.
Example: In the Tundrel template, first image on the top left), there is the sentence "Be fast, flexible, secure." And the call to action "Upgrade your Tundrel".
1) Sentence: "Your phone must ring now"
2) Sentence: "One click away from success"
3) Sentence: "Boost your income online"
4) Award: "Win new customers"
5) Sentence: "Be where your customers are looking for you"
6) Sentence: "Increase your turnover"
On the font side, it would be good to take the Tundrel banner model (in attachment) as an example by highlighting words with a larger font (vary the size of words in the same sentence to put the emphasis).
Thank you!

```html
<!DOCTYPE html>
<html lang="en">
<head>
<meta charset="utf-8">
<title>Korvi Media – Brelto Promo remarketing banners</title>
<link rel="stylesheet" href="https://fonts.googleapis.com/css2?family=Raleway:wght@400;500;700;800&display=swap">
<style>
  :root {
    --canvas: #ffffff;
    --sky: #41a9dc;
    --sky-deep: #2b86c5;
    --ocean: #2a8fd0;
    --ocean-light: #4fb3e3;
    --leaf: #8cc63f;
    --leaf-soft: #9acd4e;
    --ink: #474747;
    --bar-grey: #e9e9e9;
    --white: #ffffff;
  }
  * { box-sizing: border-box; margin: 0; padding: 0; }
  html, body {
    width: 1200px; height: 1029px; overflow: hidden;
    background: var(--canvas);
    font-family: "Raleway", Arial, sans-serif;
  }
  .banner-sheet { position: relative; width: 1200px; height: 1029px; }
  .banner {
    position: absolute; width: 520px; height: 433px; overflow: hidden;
  }
  .banner--phone { left: 77px; top: 74px; background: var(--sky); }
  .banner--click { left: 621px; top: 74px; background: linear-gradient(135deg, #3f9fd8, #2f8dcf 60%, #3a9bd7); }
  .banner--plain { left: 77px; top: 525px; background: var(--sky); }
  .banner--customers { left: 621px; top: 525px; background: radial-gradient(circle at 50% 55%, var(--ocean-light), var(--ocean) 75%); }

  .shape { position: absolute; display: block; }

  .headline {
    position: absolute; font-weight: 800; line-height: 1.12; color: var(--white);
  }
  .banner--phone .headline { left: 231px; top: 132px; font-size: 39px; letter-spacing: -0.3px; }
  .banner--click .headline {
    left: 56px; width: 410px; top: 118px; text-align: center;
    color: var(--ink); font-size: 38px; line-height: 1.16;
  }
  .banner--customers .headline {
    left: 0; width: 520px; top: 123px; text-align: center; font-size: 46px; line-height: 1.16;
  }

  .site-pill {
    position: absolute; height: 50px; border-radius: 9px;
    background: var(--leaf); color: var(--white);
    font-size: 30px; font-weight: 500; line-height: 50px; text-align: center; letter-spacing: 0.2px;
  }
  .banner--click .site-pill { left: 104px; width: 314px; top: 355px; }
  .banner--plain .site-pill { left: 101px; width: 317px; top: 362px; }
  .banner--customers .site-pill { left: 111px; width: 296px; top: 351px; }

  .browser-window {
    position: absolute; left: 56px; top: 43px; width: 410px; height: 284px;
    background: var(--white); border-radius: 6px; overflow: hidden;
    box-shadow: 0 3px 8px rgba(0,0,0,0.15);
  }
  .browser-window__bar {
    height: 24px; background: var(--bar-grey); display: flex; align-items: center; gap: 5px; padding-left: 10px;
  }
  .browser-window__dot { width: 9px; height: 9px; border-radius: 50%; }
  .browser-window__dot--blue { background: #2a7fc4; }
  .browser-window__dot--teal { background: #3bb0d8; }
  .browser-window__dot--green { background: var(--leaf); }

  .top-tab { position: absolute; left: 195px; top: 0; width: 130px; height: 104px; background: var(--white); }

  .corner-art {
    position: absolute; right: 0; bottom: 0; width: 110px; height: 170px;
    background: linear-gradient(180deg, rgba(42,143,208,0) 0%, rgba(140,198,63,0.45) 100%);
  }
</style>
</head>
<body>
<main class="banner-sheet">

  <section class="banner banner--phone" aria-label="Banner: Your phone should ring now">
    <svg class="shape" width="520" height="433" viewBox="0 0 520 433" aria-hidden="true">
      <defs>
        <linearGradient id="cta-fade" x1="0" x2="1">
          <stop offset="0" stop-color="#2f93d3"/>
          <stop offset="1" stop-color="#2f93d3" stop-opacity="0.35"/>
        </linearGradient>
      </defs>
      <circle cx="97" cy="273" r="192" fill="var(--sky-deep)"/>
      <circle cx="207" cy="99" r="27" fill="var(--leaf-soft)"/>
      <circle cx="68" cy="376" r="42" fill="var(--leaf-soft)"/>
      <circle cx="385" cy="250" r="4" fill="var(--leaf-soft)"/>
      <circle cx="520" cy="421" r="16" fill="var(--leaf-soft)"/>
      <rect x="195" y="318" width="210" height="50" fill="url(#cta-fade)"/>
      <path d="M63 316 a8 8 0 0 1 8 -8 H180 L198 343 L180 379 H71 a8 8 0 0 1 -8 -8 Z" fill="var(--white)"/>
    </svg>
    <h2 class="headline">Your phone<br>should ring<br>now.</h2>
  </section>

  <section class="banner banner--click" aria-label="Banner: One click away from success">
    <div class="browser-window">
      <div class="browser-window__bar">
        <span class="browser-window__dot browser-window__dot--blue"></span>
        <span class="browser-window__dot browser-window__dot--teal"></span>
        <span class="browser-window__dot browser-window__dot--green"></span>
      </div>
    </div>
    <h2 class="headline">One click<br>away from<br>success</h2>
    <p class="site-pill">korvimedia.ca</p>
  </section>

  <section class="banner banner--plain" aria-label="Banner: Korvi Media web address">
    <p class="site-pill">korvimedia.ca</p>
  </section>

  <section class="banner banner--customers" aria-label="Banner: Win new customers">
    <div class="top-tab"></div>
    <h2 class="headline">Win new<br>customers</h2>
    <div class="corner-art" role="img" aria-label="Space for an illustration of a hand reaching in from the corner"></div>
    <p class="site-pill">korvimedia.ca</p>
  </section>

</main>
</body>
</html>
```